Letterhead Design Project For Australian Accounting Firm

Hi All,

We need a letterhead designed for our Australian Accounting firm based in Melbourne, Victoria. I have already got a logo and business cards designed which i will add to this brief. Please design the letterhead with reference to the logo and business cards, all three items need to match. The following information needs to be included on the letterhead:

QM Advisory Logo

Suite 4 527 Harlow Street, Brunswick VIC 3056
PO Box 749, Brunswick VIC 3056

Lena Kovarik B.Com RX
Director
0491 562 804

Bartholomew Venn B.Bus RX
Director
0436 705 219

www.qmadvisory-example.com.au

at the bottom of the letterhead in small size font there needs to be the following phrase:

Liability limited by a scheme approved under Professional Standards Legislation.

Also please try and incorporate the RX logo somewhere on the letterhead

We are looking for a sharp and modern looking letterhead design, something that incorporates the look of the business card and logo.

Thanks.

```html
<!DOCTYPE html>
<html lang="en">
<head>
<meta charset="utf-8">
<title>QM Advisory Letterhead</title>
<link rel="stylesheet" href="https://fonts.googleapis.com/css2?family=Arimo:wght@400;700&family=Open+Sans:wght@400;600;700&display=swap">
<style>
  :root {
    --backdrop: #e9e6e1;
    --paper: #ffffff;
    --ink: #1a1a1a;
    --muted: #555555;
    --band-grey: #dcdcdc;
    --rule-grey: #9a9a9a;
    --accent-red: #d4202a;
    --footer-black: #0d0d0d;
    --footer-text: #d8d8d8;
  }
  * { box-sizing: border-box; margin: 0; padding: 0; }
  html, body {
    width: 1099px;
    height: 1200px;
    overflow: hidden;
    background: var(--backdrop);
  }
  .letterhead {
    position: absolute;
    left: 130px;
    top: 20px;
    width: 840px;
    height: 1160px;
    background: var(--paper);
    box-shadow: 0 2px 10px rgba(0,0,0,0.12);
    overflow: hidden;
    color: var(--ink);
    font-family: "Arimo", Arial, sans-serif;
  }
  .address-band {
    position: absolute;
    left: 0;
    top: 58px;
    width: 345px;
    height: 40px;
    background: var(--band-grey);
    padding: 6px 0 0 95px;
    font-family: "Open Sans", Arial, sans-serif;
    font-size: 9.5px;
    line-height: 13px;
    color: #444;
    white-space: nowrap;
  }
  .brand {
    position: absolute;
    left: 358px;
    top: 50px;
    display: flex;
    align-items: center;
    font-family: "Open Sans", Arial, sans-serif;
  }
  .brand-name {
    font-size: 21px;
    font-weight: 700;
    color: var(--ink);
    letter-spacing: 0.5px;
    line-height: 1;
    padding-right: 12px;
    white-space: nowrap;
  }
  .brand-divider {
    width: 1px;
    height: 50px;
    background: var(--ink);
    flex: none;
  }
  .brand-tagline {
    padding-left: 10px;
    font-size: 11px;
    font-weight: 600;
    line-height: 14px;
    color: var(--ink);
    white-space: nowrap;
  }
  .member-badge {
    flex: none;
    width: 26px;
    height: 26px;
    margin-left: 22px;
  }
  .edge-tab {
    position: absolute;
    right: 0;
    width: 26px;
    background: var(--accent-red);
  }
  .edge-tab.top { top: 40px; height: 66px; }
  .edge-tab.lower { top: 832px; height: 96px; }
  .letter-body {
    position: absolute;
    left: 95px;
    top: 218px;
    width: 640px;
    font-size: 14.5px;
    line-height: 19px;
  }
  .letter-body p { margin-bottom: 19px; }
  .salutation { margin-bottom: 24px; }
  .salutation strong { font-weight: 700; display: block; }
  .signature-area {
    position: absolute;
    left: 578px;
    top: 838px;
    width: 140px;
    height: 46px;
    background: #ececec;
  }
  .directors {
    position: absolute;
    left: 95px;
    top: 840px;
    padding-left: 14px;
    border-left: 3px solid var(--rule-grey);
    font-family: "Open Sans", Arial, sans-serif;
    font-size: 10.5px;
    line-height: 14px;
    color: var(--ink);
  }
  .director { margin-bottom: 12px; }
  .director:last-child { margin-bottom: 0; }
  .director-name { font-weight: 700; text-transform: uppercase; letter-spacing: 0.4px; }
  .director-qual { font-style: italic; color: var(--muted); font-size: 9.5px; }
  .label { font-weight: 700; }
  .website {
    position: absolute;
    left: 95px;
    top: 990px;
    font-family: "Open Sans", Arial, sans-serif;
    font-size: 11px;
    color: var(--ink);
  }
  .website .domain { color: var(--accent-red); font-weight: 700; }
  .footer-band {
    position: absolute;
    left: 0;
    bottom: 0;
    width: 100%;
    height: 140px;
    background: var(--footer-black);
    padding-top: 18px;
    text-align: center;
    font-family: "Open Sans", Arial, sans-serif;
    font-size: 11px;
    letter-spacing: 1.2px;
    color: var(--footer-text);
  }
</style>
</head>
<body>
  <main class="letterhead">
    <div class="address-band">
      Suite 4 527 Harlow Street, Brunswick VIC 3056<br>
      PO Box 749, Brunswick VIC 3056
    </div>

    <div class="brand">
      <span class="brand-name">QM Advisory</span>
      <span class="brand-divider"></span>
      <span class="brand-tagline">TAXATION AND<br>BUSINESS SERVICES</span>
      <svg class="member-badge" viewBox="0 0 26 26" role="img" aria-label="Professional membership badge">
        <circle cx="13" cy="13" r="12" fill="var(--accent-red)"/>
      </svg>
    </div>

    <div class="edge-tab top"></div>
    <div class="edge-tab lower"></div>

    <section class="letter-body">
      <div class="salutation">Lorem<strong>ipsum dolor sit amet,</strong></div>
      <p>consectetur adipiscing elit. Duis facilisis elementum dui, bibendum pulvinar nulla malesuada quis. Curabitur ut leo quam. Pellentesque laoreet metus risus, non fermentum arcu malesuada vitae. Vestibulum dui libero, vestibulum non quam sit amet, auctor lobortis tortor. Integer blandit enim vitae adipiscing adipiscing. Vivamus metus lacus, porta at aliquam sit amet,</p>
      <p>pretium ut eros. Curabitur a dui interdum, elementum urna ut, venenatis erat. Fusce feugiat odio sed dui rhoncus auctor. Aenean posuere, odio ut facilisis tempus, nunc mauris convallis lacus, eget vulputate enim purus ac odio. Donec blandit et ipsum a aliquet. Mauris semper diam in velit vestibulum, sit amet molestie purus convallis. Duis pulvinar porttitor magna in malesuada.</p>
      <p>Nullam auctor neque orci, nec ornare odio auctor et. Phasellus eu sapien nec nibh lobortis commodo. Donec nec commodo nibh. Sed nec nulla et magna fermentum suscipit. Nam ligula nunc, facilisis iaculis venenatis eget,</p>
      <p>gravida consectetur odio. Donec in leo ac felis vestibulum feugiat. In at orci id justo adipiscing vehicula. Sed tortor purus, pellentesque vel lobortis nec, tincidunt vitae mi. Duis pellentesque augue vitae pharetra euismod.</p>
      <p>Duis vulputate, libero nec vehicula pretium, mi nisi tristique mauris, ac porttitor diam metus at ante. Pellentesque magna arcu, viverra ac lacinia nec, pharetra id est. Maecenas ullamcorper mattis tellus, et dapibus arcu sagittis malesuada.</p>
      <p>ada fames ac ante ipsum primis in faucibus. Morbi sodales accumsan risus, nec condimentum lorem faucibus a.</p>
    </section>

    <div class="signature-area" role="img" aria-label="Handwritten signature of the sender"></div>

    <section class="directors">
      <div class="director">
        <div><span class="director-name">Lena Kovarik</span> <span class="director-qual">B.Com RX</span></div>
        <div>Director</div>
        <div><span class="label">Phone:</span> 0491 562 804</div>
      </div>
      <div class="director">
        <div><span class="director-name">Bartholomew Venn</span> <span class="director-qual">B.Bus RX</span></div>
        <div>Director</div>
        <div><span class="label">Phone:</span> 0436 705 219</div>
      </div>
    </section>

    <div class="website">www.<span class="domain">qmadvisory-example</span>.com.au</div>

    <footer class="footer-band">Liability limited by a scheme approved under Professional Standards Legislation</footer>
  </main>
</body>
</html>
```